Homepage layout for online ad network

Attached is our Calvrex Media logo and updated brief (I can't seem to delete the old logo and brief, but they're no longer relevant).

This project was originally posted with a different logo and corporate name, but we have decided to stay with our current logo and name and redesign the site.

Your design is for a homepage only - design, no coding (I'll get someone else to take your PSD and code it).

Your homepage will make use of a Flash slider - BUT YOU ARE NOT REQUIRED TO PROVIDE THE FLASH. Instead, simply provide the layout and at least two static examples out of the four different sections that will eventually be in the slider.

Much of this design is based on the design of a competitor (listed in the brief).

Please ask whatever questions you need to in order to clarify instructions.
Updates

Project updated to include new logo (and correspondingly new color scheme).

Brief changed slightly.

Thank you for submitting designs for this project in the past.

After some internal strategy work, we have decided to retain our initial corporate identity, Calvrex Media.

If you have submitted a design for the original brief and are available, please re-work your best prior design to reflect the color scheme in the newly uploaded logo.

Target Market(s)

This site is aimed primarily at young professionals who buy digital media on behalf of large advertisers.

Industry/Entity Type

Media

Requirements
Must have
• modern white space
Should not have
• no Flash outside of slider

```html
<!DOCTYPE html>
<html lang="en">
<head>
<meta charset="utf-8">
<title>Calvrex Media</title>
<link href="https://fonts.googleapis.com/css2?family=Arimo:wght@400;700&family=Teko:wght@400;500&display=swap" rel="stylesheet">
<style>
:root{
  --ink:#111;
  --red:#c4080d;
  --red-dark:#6e0002;
  --red-text:#d0100f;
  --news-blue:#0b76b4;
  --news-bar:#0d2a3e;
  --card:#161616;
  --white:#fff;
}
*{margin:0;padding:0;box-sizing:border-box}
html,body{width:1200px;height:900px;overflow:hidden;background:#fff;font-family:"Arimo",Arial,sans-serif;color:var(--ink)}
.page{position:relative;width:1200px;height:900px;overflow:hidden;background:linear-gradient(#fff 450px,#f4f4f4 520px,#fff 700px)}

.top-bar{position:absolute;left:0;top:0;width:1200px;height:110px;
  background:repeating-linear-gradient(45deg,#222 0 2px,#161616 2px 4px)}
.nav-band{position:absolute;left:0;top:110px;width:1200px;height:35px;
  background:linear-gradient(var(--red) 0%,#a70004 50%,var(--red-dark) 100%);border-top:1px solid #e22}
.main-nav{position:absolute;right:122px;top:119px;color:#fff;font-weight:700;font-size:14px;display:flex;gap:7px}
.main-nav span.sep{font-weight:400}

.logo-tab{position:absolute;left:112px;top:0;width:251px;height:118px;background:#fff;
  border-radius:0 0 10px 10px;box-shadow:0 3px 8px rgba(0,0,0,.5)}
.logo-mark{position:absolute;left:22px;top:38px;width:26px;height:26px;background:var(--red)}
.logo-name{position:absolute;left:58px;top:38px;font-size:24px;line-height:26px;font-weight:400;color:var(--red);white-space:nowrap}
.logo-tag{position:absolute;left:22px;top:89px;font-size:11px;color:var(--red)}

.hero{position:absolute;left:0;top:145px;width:1200px;height:271px;
  background:linear-gradient(#cfcfcf 0%,#fff 50%,#c4c4c4 100%)}
.hero-photo{position:absolute;left:112px;top:125px;width:364px;height:291px;
  background:radial-gradient(ellipse at 45% 60%,#2a2a2a 0 35%,rgba(60,60,60,.6) 55%,rgba(200,200,200,0) 72%)}
.hero-title{position:absolute;left:512px;top:222px;font-size:100px;line-height:100px;font-weight:400;letter-spacing:-3px;white-space:nowrap}
.hero-note{position:absolute;left:527px;top:324px;font-size:11px;color:#666;letter-spacing:.8px;white-space:nowrap}
.hero-band{position:absolute;left:0;top:416px;width:1200px;height:37px;
  background:linear-gradient(var(--red) 0%,#a40003 60%,var(--red-dark) 100%);box-shadow:0 4px 8px rgba(0,0,0,.15)}

.about{position:absolute;left:135px;top:497px;width:640px}
.about h1{font-size:29px;font-weight:400;line-height:34px;margin-bottom:2px}
.about p{font-size:12.2px;line-height:17px;margin-bottom:17px}
.btn-more{position:absolute;display:block;width:76px;height:20px;border-radius:2px;
  background:linear-gradient(#e1262a,#a80306);color:#fff;font-size:9px;font-weight:700;text-align:center;line-height:20px;letter-spacing:.5px;
  box-shadow:2px 2px 3px rgba(0,0,0,.45)}
.divider{position:absolute;left:121px;top:721px;width:665px;height:1px;background:#999}

.cat-title{position:absolute;top:742px;width:153px;text-align:center;font-family:"Teko",sans-serif;font-weight:400;font-size:34px;line-height:40px;letter-spacing:2px;color:var(--red-text)}
.cat-card{position:absolute;top:783px;width:153px;height:140px;background:var(--card);box-shadow:0 0 6px rgba(0,0,0,.5)}
.cat-card .photo{position:absolute;left:8px;top:9px;width:135px;height:58px}
.cat-card h3{position:absolute;left:15px;top:76px;font-size:11px;color:var(--red-text);font-weight:400}
.cat-card p{position:absolute;left:15px;top:95px;width:130px;font-size:9px;line-height:11px;color:#fff}

.news{position:absolute;left:797px;top:490px;width:297px;height:430px;border-radius:8px;
  background:linear-gradient(90deg,#0a6aa3,var(--news-blue) 10%,var(--news-blue) 90%,#0a6aa3);box-shadow:0 0 8px rgba(0,0,0,.35)}
.news-icon{position:absolute;left:22px;top:20px;width:34px;height:26px}
.news h2{position:absolute;left:65px;top:24px;color:#fff;font-size:17px;font-weight:400}
.news-date{position:absolute;left:14px;top:56px;width:268px;height:34px;background:var(--news-bar);color:#fff;font-weight:700;font-size:13px;line-height:34px;padding:0 18px 0 27px;display:flex;justify-content:space-between}
.news-item{position:absolute;left:26px;width:255px}
.news-item h4{font-size:13.5px;color:#fff;text-decoration:underline;padding-left:18px;position:relative;margin-bottom:6px}
.news-item h4::before{content:"";position:absolute;left:0;top:3px;width:9px;height:9px;border:1px solid #fff;background:var(--news-bar)}
.news-item p{font-size:12.2px;line-height:19px;color:#0b1e2e}
</style>
</head>
<body>
<div class="page">
  <div class="top-bar"></div>
  <div class="nav-band"></div>
  <nav class="main-nav"><span>Beauty</span><span class="sep">|</span><span>Cooking</span><span class="sep">|</span><span>Parenting</span><span class="sep">|</span><span>Video</span></nav>

  <div class="logo-tab">
    <div class="logo-mark"></div>
    <div class="logo-name">Calvrex Media</div>
    <div class="logo-tag">audiences built for every advertiser</div>
  </div>

  <section class="hero"></section>
  <div class="hero-photo" role="img" aria-label="Magician in tailcoat holding a wand and top hat"></div>
  <div class="hero-title">WELCOME</div>
  <div class="hero-note">*all gray area can be flash movie, browser wide. With or without top meni in red bar.</div>
  <div class="hero-band"></div>

  <section class="about">
    <h1>Who we are ?</h1>
    <p><b>turpis. Sed tristique. Integer nulla nisl, dapibus et, interdum vel,</b> sollicitudin in, dui. Nullam venatis, augue at viverra egestas, lacus neque molestie metus, eu tincidunt ipsum nisi vitae tellus.</p>
    <p>Nullam eget nulla. Phasellus id dolor. Mauris molestie. Aliquam vitae felis in pede congue auctor. Phaselluut pede id orci aliquam adipiscing. Sed dolor dui, dapibus quis, nonummy non, gravidarton sollicitudin, mauris. Nam cursus. Integer lobortis, est at rhoncus auctor, tortor odio hendrerit orci, non malesuada nisl ipsum in nunc. Curabitur arcu justo, euismod vel, tempor eget, volutpatoncupat tincidunt, odio.</p>
  </section>
  <span class="btn-more" style="left:681px;top:669px">READ MORE</span>
  <div class="divider"></div>

  <div class="cat-title" style="left:123px">BEAUTY</div>
  <div class="cat-title" style="left:291px">COOKING</div>
  <div class="cat-title" style="left:459px">PARENTING</div>
  <div class="cat-title" style="left:627px">VIDEO</div>

  <article class="cat-card" style="left:123px">
    <div class="photo" role="img" aria-label="Smiling woman outdoors" style="background:linear-gradient(90deg,#5a8a2a,#d9b46a 60%,#6f9b3a)"></div>
    <h3>Cras lacinia nunc in</h3>
    <p>Bandit aenean commodo vulputate ante proin</p>
  </article>
  <article class="cat-card" style="left:291px">
    <div class="photo" role="img" aria-label="Cutting vegetables on a board" style="background:linear-gradient(90deg,#a8664a,#e8d6c2 55%,#c9a070)"></div>
    <h3>Ad litora torquent</h3>
    <p>Faucibus odio sit ametue maecenas</p>
  </article>
  <article class="cat-card" style="left:459px">
    <div class="photo" role="img" aria-label="Child with parent" style="background:linear-gradient(90deg,#d9a060,#e8c9a0 50%,#3c6fb0)"></div>
    <h3>Maecenas eu</h3>
    <p>Bandit aenean commodo vulputate ante proin</p>
  </article>
  <article class="cat-card" style="left:627px">
    <div class="photo" role="img" aria-label="Film clapperboard and woman" style="background:linear-gradient(90deg,#2a2a2a,#8a8a8a 45%,#3a6aa8)"></div>
    <h3>Sapien egestas conval</h3>
    <p>Hendrerit turpis non lacus praesent convallis</p>
  </article>

  <aside class="news">
    <svg class="news-icon" viewBox="0 0 34 26"><rect x="3" y="4" width="26" height="19" fill="#f2f2f2" stroke="#ccc" transform="rotate(-12 16 13)"/><g stroke="#999" stroke-width="1.5" transform="rotate(-12 16 13)"><line x1="7" y1="9" x2="25" y2="9"/><line x1="7" y1="13" x2="25" y2="13"/><line x1="7" y1="17" x2="20" y2="17"/></g></svg>
    <h2>Latest News</h2>
    <div class="news-date"><span>ON 12 OCTOBER 2010</span><span>London</span></div>
    <div class="news-item" style="top:104px">
      <h4>Lorem ipsum dolor sit amet</h4>
      <p>varius vitae, orci. Donec arcu elit, placerat ac, pulvinar et, lacinia eu, risus.</p>
    </div>
    <span class="btn-more" style="left:201px;top:166px">READ MORE</span>
    <div class="news-item" style="top:196px">
      <h4>Lorem ipsum dolor sit amet</h4>
      <p>blandit dui. Proin elit lorem, blandit id, volutpat vel, facilisis sed, enim. Aenean nonummy volutpat eros.</p>
    </div>
    <span class="btn-more" style="left:201px;top:272px">READ MORE</span>
    <div class="news-item" style="top:301px">
      <h4>Convallis pellentesque uspendisse</h4>
      <p>varius vitae, orci. Donec arcu elit, placerat ac, pulvinar et, lacinia eu, risus. Quisque rhoncus ultrices lorem. Fusce facilisis, sem vitae condimentum</p>
    </div>
    <span class="btn-more" style="left:201px;top:396px">READ MORE</span>
  </aside>
</div>
</body>
</html>
```